Fashion clothing business needs a label, swing tag and business card.

Independent womenswear label called "Tessa Wrenly".
I'd like a design for a woven label to go on the clothes, a swing tag and business card design. The design should be simple, modern but timeless. Its a small business, made locally in Melbourne, Australia, produces quality garments for everyday wear using beautiful fabrics.

Reason: just waiting for a few others to submit their designs.

Target Market(s)

30+ ladies, who want quality everyday wear, who don't necessarily follow trends. They can be a bit edgy and willing to take a risk with something different.

Industry/Entity Type

Clothing

Font styles to use
Other font styles liked:
• I dont mind the typewriter font, but can it look modern? happy for you to choose.

Requirements
Should not have
• A difficult shape swing tag - as it might be more expensive for me to get printed and cut.

```html
<!DOCTYPE html>
<html lang="en">
<head>
<meta charset="utf-8">
<title>Tessa Wrenly – Label, Swing Tag and Business Card</title>
<link rel="stylesheet" href="https://fonts.googleapis.com/css2?family=Arimo:wght@400;700&display=swap">
<style>
  :root {
    --brand-magenta: #b3178f;
    --paper-white: #ffffff;
    --canvas-bg: #f2f0f1;
    --tag-edge: #c9c6c8;
    --hole-grey: #e6e3e5;
  }
  * { box-sizing: border-box; margin: 0; padding: 0; }
  html, body { width: 1200px; height: 900px; overflow: hidden; }
  body {
    background: var(--canvas-bg);
    font-family: "Arimo", Arial, sans-serif;
    position: relative;
  }

  /* Swing tags */
  .swing-tag {
    position: absolute;
    top: 260px;
    width: 195px;
    height: 398px;
    border-radius: 26px;
  }
  .swing-tag--front { left: 30px; background: var(--brand-magenta); color: var(--paper-white); }
  .swing-tag--back { left: 290px; background: var(--paper-white); border: 1.5px solid var(--tag-edge); color: var(--brand-magenta); }

  .tag-mark {
    position: absolute;
    top: 22px; left: 50%;
    width: 62px; height: 62px;
    margin-left: -31px;
    border-radius: 50%;
  }
  .swing-tag--front .tag-mark { background: var(--paper-white); }
  .swing-tag--back .tag-mark { background: var(--brand-magenta); }
  .tag-hole {
    position: absolute;
    top: 46px; left: 50%;
    width: 14px; height: 14px;
    margin-left: -7px;
    border-radius: 50%;
    background: var(--hole-grey);
  }

  .tag-name {
    position: absolute;
    top: 100px; left: 86px;
    writing-mode: vertical-rl;
    font-weight: 700;
    font-size: 44px;
    letter-spacing: -0.5px;
    white-space: nowrap;
  }
  .tag-origin, .tag-email {
    position: absolute;
    writing-mode: vertical-rl;
    font-size: 13px;
    white-space: nowrap;
  }
  .tag-origin { top: 250px; left: 60px; }
  .tag-email { top: 185px; left: 42px; }

  .tag-fields {
    position: absolute;
    top: 160px; left: 20px;
    list-style: none;
    font-size: 14px;
  }
  .tag-fields li { margin-bottom: 20px; }

  /* Business card */
  .business-card {
    position: absolute;
    top: 70px; left: 640px;
    width: 500px; height: 286px;
    border-radius: 16px;
    background: var(--brand-magenta);
    color: var(--paper-white);
  }
  .card-mark {
    position: absolute;
    top: 38px; right: 38px;
    width: 74px; height: 74px;
    border-radius: 50%;
    background: var(--paper-white);
  }
  .card-name {
    position: absolute;
    top: 100px; left: 36px;
    font-weight: 700;
    font-size: 54px;
    letter-spacing: -0.5px;
    white-space: nowrap;
  }
  .card-contact {
    position: absolute;
    top: 176px; left: 38px;
    font-size: 14px;
    line-height: 1.45;
  }

  /* Woven label */
  .woven-label {
    position: absolute;
    top: 570px; left: 750px;
    width: 226px; height: 128px;
    border-radius: 8px;
    background: var(--brand-magenta);
    color: var(--paper-white);
    padding: 38px 0 0 12px;
  }
  .label-name {
    font-weight: 700;
    font-size: 32px;
    letter-spacing: -0.3px;
    white-space: nowrap;
    line-height: 1;
  }
  .label-origin { font-size: 14px; margin-top: 4px; }
</style>
</head>
<body>

  <section class="swing-tag swing-tag--front" aria-label="Swing tag, front">
    <span class="tag-mark"></span>
    <span class="tag-hole"></span>
    <p class="tag-name">Tessa Wrenly</p>
    <p class="tag-origin">Made in Australia</p>
    <p class="tag-email">email: info@tessawrenly.com</p>
  </section>

  <section class="swing-tag swing-tag--back" aria-label="Swing tag, back">
    <span class="tag-mark"></span>
    <span class="tag-hole"></span>
    <ul class="tag-fields">
      <li>Size.......</li>
      <li>style......</li>
      <li>Price.....</li>
    </ul>
  </section>

  <section class="business-card" aria-label="Business card">
    <span class="card-mark"></span>
    <p class="card-name">Tessa Wrenly</p>
    <p class="card-contact">mob: 0400123987<br>email: info@tessawrenly.com</p>
  </section>

  <section class="woven-label" aria-label="Woven garment label">
    <p class="label-name">Tessa Wrenly</p>
    <p class="label-origin">Made in Australia</p>
  </section>

</body>
</html>
```